Become an EMT and Serve your community!

We are looking to design a postcard that will be mailed to surrounding communities that notifies them of our upcoming EMT class with an emphasis of serving their community. We are looking for a design that grabs peoples attention and motivates them to sign up and serve their community. Our primary colors are red and blue. We would like to incorporate the Institute logo as well as one or two photos. We do have more photos available upon request. Our Institute website is www.halvorsenacademy.net for more material. It is important that the postcard meets mailing guidelines.

Target Market(s)

Local community members

Industry/Entity Type

Education

Font styles to use
Sans Serif

Colors
f04a50
3176b5
0255a3
eaf1f7

Requirements
Must have
• Dates
Prices
Contact info
Look interesting
Convey the message of “Serving your Community”
Nice to have
• Clear information
Concise
Incorporate an action shot
Should not have
• Generic EMS logos

```html
<!DOCTYPE html>
<html lang="en">
<head>
<meta charset="utf-8">
<title>2020 Summer EMT Class Postcard</title>
<link href="https://fonts.googleapis.com/css2?family=Open+Sans:wght@400;600;700;800&family=Libre+Baskerville&display=swap" rel="stylesheet">
<style>
  :root {
    --red: #d71f2b;
    --red-bright: #f04a50;
    --blue: #0255a3;
    --navy: #1d2a7a;
    --blue-mid: #3176b5;
    --pale: #eaf1f7;
    --white: #ffffff;
    --ink: #1d2a5e;
    --stage: #8e8e8e;
  }
  * { box-sizing: border-box; margin: 0; padding: 0; }
  html, body { width: 1200px; height: 1030px; overflow: hidden; }
  body {
    background: var(--stage);
    font-family: "Open Sans", Arial, sans-serif;
    position: relative;
  }
  .postcard {
    position: absolute;
    top: 311px;
    width: 570px;
    height: 407px;
    background: var(--white);
    overflow: hidden;
    box-shadow: 0 6px 14px rgba(0,0,0,.35);
  }
  .postcard--front { left: 20px; }
  .postcard--back { left: 610px; }
  .postcard > svg.shapes { position: absolute; inset: 0; }
  .t { position: absolute; white-space: nowrap; }

  /* front */
  .brand { left: 14px; top: 18px; display: flex; flex-direction: column; gap: 10px; }
  .brand-row { display: flex; align-items: center; gap: 8px; font-weight: 700; font-size: 12px; color: var(--navy); line-height: 1.2; white-space: normal; width: 185px; }
  .brand-row .dot { width: 34px; height: 34px; border-radius: 50%; background: var(--navy); flex: none; }
  .brand-row .sq { width: 34px; height: 34px; background: var(--red); flex: none; }
  .presents { left: 0; width: 215px; top: 124px; text-align: center; font-family: "Libre Baskerville", Georgia, serif; font-size: 24px; color: var(--navy); }
  .season { left: 13px; top: 190px; font-size: 27px; font-weight: 800; color: var(--red-bright); }
  .title { left: 12px; top: 218px; font-size: 40px; font-weight: 600; color: var(--white); letter-spacing: .5px; }
  .when { left: 79px; top: 269px; background: var(--red); color: var(--white); font-weight: 700; font-size: 14px; padding: 0 13px; border-radius: 10px; line-height: 19px; }
  .days { left: 0; width: 215px; top: 294px; text-align: center; line-height: 17px; font-size: 13.5px; font-weight: 700; color: var(--white); }
  .days .span { color: var(--red-bright); font-weight: 600; }
  .lab-note { left: 234px; top: 223px; width: 176px; height: 64px; border: 1.5px dashed var(--white); border-radius: 12px; color: var(--white); font-size: 10px; line-height: 12.5px; text-align: center; padding-top: 6px; white-space: normal; }
  .weekend { left: 236px; width: 190px; top: 297px; text-align: center; color: var(--white); font-size: 9px; line-height: 12px; }
  .weekend b { font-size: 12px; }
  .tuition { left: 428px; top: 202px; width: 129px; text-align: center; color: var(--white); font-size: 10.5px; line-height: 13px; white-space: normal; }
  .tuition .price { font-size: 18px; font-weight: 700; line-height: 22px; }
  .contact { font-size: 13.5px; color: var(--navy); display: flex; align-items: center; gap: 5px; }
  .contact svg { flex: none; }
  .follow { color: var(--white); font-size: 10.5px; font-weight: 600; letter-spacing: .8px; }

  /* back */
  .sender { left: 338px; top: 14px; width: 156px; text-align: center; color: var(--navy); font-size: 8px; line-height: 10px; white-space: nowrap; }
  .sender .name { font-weight: 700; font-size: 9.5px; display: flex; align-items: center; justify-content: center; gap: 4px; margin-bottom: 2px; }
  .sender .name i { width: 12px; height: 12px; border-radius: 50%; background: var(--navy); display: inline-block; flex: none; }
  .stamp { left: 502px; top: 13px; width: 52px; height: 62px; border: 1.5px solid #111; }
  .serve { left: 12px; top: 258px; font-size: 21px; font-weight: 800; color: var(--white); letter-spacing: .3px; }
  .blurb { left: 13px; top: 285px; width: 300px; font-size: 8.5px; line-height: 11px; color: var(--white); white-space: normal; }
  .back-contact { left: 15px; top: 337px; color: var(--white); font-size: 11px; line-height: 14px; }
  .back-contact div { display: flex; align-items: center; gap: 4px; }
</style>
</head>
<body>

<section class="postcard postcard--front" aria-label="Postcard front">
  <svg class="shapes" viewBox="0 0 570 407" width="570" height="407">
    <defs>
      <linearGradient id="photoFront" x1="0" y1="0" x2="1" y2="1">
        <stop offset="0" stop-color="#cfd3d6"/>
        <stop offset=".5" stop-color="#a99a8e"/>
        <stop offset="1" stop-color="#6f7075"/>
      </linearGradient>
      <linearGradient id="bandFront" x1="0" y1="0" x2="1" y2="0">
        <stop offset="0" stop-color="#1f3d94"/>
        <stop offset="1" stop-color="#1d2a7a"/>
      </linearGradient>
    </defs>
    <rect x="218" y="0" width="352" height="200" fill="url(#photoFront)" role="img" aria-label="Photo of EMT students practising CPR on training manikins"/>
    <path d="M0 190 C120 150 300 160 570 115 V140 C300 190 120 178 0 215 Z" fill="var(--red)"/>
    <path d="M0 205 C120 172 300 182 570 132 V362 H0 Z" fill="url(#bandFront)"/>
    <path d="M0 197 C120 162 300 172 570 124" stroke="var(--white)" stroke-width="3" fill="none"/>
    <rect x="214" y="0" width="4" height="183" fill="var(--red)"/>
    <polygon points="426,186 559,160 559,315 500,298 426,312" fill="var(--red)"/>
    <rect x="0" y="362" width="570" height="45" fill="var(--white)"/>
    <polygon points="224,407 236,385 430,385 444,407" fill="var(--red)"/>
    <polyline points="470,362 502,362 508,340 514,395 522,330 528,362 570,362" fill="none" stroke="var(--red)" stroke-width="2.5"/>
    <circle cx="467" cy="395" r="10" fill="var(--navy)"/>
    <circle cx="495" cy="395" r="10" fill="var(--blue-mid)"/>
  </svg>

  <div class="t brand">
    <div class="brand-row"><span class="dot"></span>Halvorsen Academy of EMS</div>
    <div class="brand-row"><span class="sq"></span>Halvorsen Memorial EMS</div>
  </div>
  <div class="t presents">Presents</div>

  <div class="t season">2020 SUMMER</div>
  <div class="t title">EMT CLASS</div>
  <div class="t when">WHEN</div>
  <div class="t days">Monday, Tuesday,Wednesday<br><span class="span">from May 26th through<br>August 17th</span></div>

  <div class="t lab-note">Wednesdays:<br>Students will need to sign up for either a 4:00p-7:00p lab section, or a 7:00p-10:0p lab section.</div>
  <div class="t weekend">There will be one required Sat/Sun<br>weekend held for all students.<br>This will take place on <b>June 13th &amp; 14th</b><br>Weekend classes will run from 8:00am -8:00pm.</div>

  <div class="t tuition">Tuition<br><span class="price">$1000 EMT</span><br>(without CPR).<br><b style="font-size:13px">$250</b> <b>deposit</b> is due at time of registration</div>

  <div class="t contact" style="left:15px;top:366px">
    <svg width="12" height="12" viewBox="0 0 24 24"><path d="M6.6 10.8a15.1 15.1 0 0 0 6.6 6.6l2.2-2.2a1 1 0 0 1 1-.25 11.4 11.4 0 0 0 3.6.57 1 1 0 0 1 1 1V20a1 1 0 0 1-1 1A17 17 0 0 1 3 4a1 1 0 0 1 1-1h3.5a1 1 0 0 1 1 1c0 1.250.2 2.45.57 3.57a1 1 0 0 1-.25 1z" fill="var(--red)"/></svg>(555) 014-2290</div>
  <div class="t contact" style="left:15px;top:384px">
    <svg width="12" height="12" viewBox="0 0 24 24"><circle cx="12" cy="12" r="9" fill="none" stroke="var(--red)" stroke-width="2.5"/><path d="M3 12h18M12 3c3 3 3 15 0 18M12 3c-3 3-3 15 0 18" stroke="var(--red)" stroke-width="2" fill="none"/></svg>www.halvorsenacademy.net</div>
  <div class="t contact" style="left:240px;top:364px">
    <svg width="12" height="10" viewBox="0 0 24 18"><rect width="24" height="18" rx="2" fill="var(--red)"/><path d="M1 2l11 8 11-8" stroke="#fff" stroke-width="2" fill="none"/></svg>info@halvorsenems.org</div>
  <div class="t follow" style="left:246px;top:388px">follow us on social media</div>
</section>

<section class="postcard postcard--back" aria-label="Postcard back">
  <svg class="shapes" viewBox="0 0 570 407" width="570" height="407">
    <defs>
      <linearGradient id="photoBack" x1="0" y1="0" x2="1" y2="1">
        <stop offset="0" stop-color="#d6dade"/>
        <stop offset=".55" stop-color="#8c8a93"/>
        <stop offset="1" stop-color="#b2323c"/>
      </linearGradient>
    </defs>
    <path d="M0 0 H300 C340 50 345 150 318 232 H0 Z" fill="url(#photoBack)" role="img" aria-label="Photo of an instructor teaching a group of students beside a red ambulance"/>
    <path d="M0 228 H320 C314 260 308 300 303 335 H0 Z" fill="var(--red)"/>
    <path d="M0 335 H303 C298 370 290 395 272 407 H0 Z" fill="var(--navy)"/>
    <path d="M300 0 C345 50 350 150 320 232 C308 300 300 380 272 407" stroke="var(--red)" stroke-width="4" fill="none"/>
    <polygon points="0,407 0,385 200,385 212,407" fill="var(--red)"/>
    <circle cx="235" cy="390" r="10" fill="var(--blue-mid)"/>
    <circle cx="262" cy="390" r="10" fill="var(--blue-mid)"/>
  </svg>

  <div class="t sender">
    <div class="name"><i></i>Halvorsen Academy of EMS</div>
    12 Linden Avenue Brookfield, NH 03000
  </div>
  <div class="t stamp"></div>

  <div class="t serve">SERVE YOUR COMMUNITY</div>
  <div class="t blurb">and become an Emergency Medical Technician. As a student you will have access to cutting edge training equipment, experienced instructors, and be able to train on a <b>911 Ambulance</b> through <b>Halvorsen EMS.</b></div>
  <div class="t back-contact">
    <div><svg width="10" height="10" viewBox="0 0 24 24"><path d="M6.6 10.8a15.1 15.1 0 0 0 6.6 6.6l2.2-2.2a1 1 0 0 1 1-.25 11.4 11.4 0 0 0 3.6.57 1 1 0 0 1 1 1V20a1 1 0 0 1-1 1A17 17 0 0 1 3 4a1 1 0 0 1 1-1h3.5a1 1 0 0 1 1 1c0 1.25.2 2.45.57 3.57a1 1 0 0 1-.25 1z" fill="var(--red-bright)"/></svg>(555) 014-2290</div>
    <div><svg width="10" height="10" viewBox="0 0 24 24"><circle cx="12" cy="12" r="9" fill="none" stroke="var(--red-bright)" stroke-width="2.5"/><path d="M3 12h18M12 3c3 3 3 15 0 18M12 3c-3 3-3 15 0 18" stroke="var(--red-bright)" stroke-width="2" fill="none"/></svg>www.halvorsenacademy.net</div>
    <div><svg width="10" height="8" viewBox="0 0 24 18"><rect width="24" height="18" rx="2" fill="var(--red-bright)"/><path d="M1 2l11 8 11-8" stroke="#fff" stroke-width="2" fill="none"/></svg>info@halvorsenems.org</div>
  </div>
  <div class="t follow" style="left:32px;top:388px">follow us on social media</div>
</section>

</body>
</html>
```